Brisk Lyceum Website

We are looking for a new design of our website. The current website is www.brisklyceum-example.com. The company is the #1 pre-college math and science program in Orange County, CA. We would like to see designs that integrate our logo with a modern color scheme. We are also open for suggestions that could improve our logo. We would like a simple, minimal, clean, classy, and vibrant front-page user interface design that give the premium, modern, innovative, creative, and premier brand feel. We like the "New Retro Colors for the Web" as described here: http://www.pixelharbor-example.net/en/layout-notes-2013/.

Target Market(s)

The target market is parents with K-12 students from a diverse population. Parents are well educated with family income > $150,000. Most of the decision makers are mothers from immigrate families: 30% Chinese, 30% Korean, 15% Indian, 24% White.

Industry/Entity Type

College

Requirements
Must have
• Must read our statement of differentiation at:
• http://brisklyceum-example.com/about-us
• Your design must be reflective of your understanding of the statements.
Nice to have
• The design should also be mobil friendly.
Should not have
• While most of our current classes are math, our company is expanding to include STEM (Science, Technology, Engineering, and Math) for gifted students. Therefore, the site should not be JUST a math education site.

```html
<!DOCTYPE html>
<html lang="en">
<head>
<meta charset="utf-8">
<title>Brisk Lyceum for Gifted Youth</title>
<link href="https://fonts.googleapis.com/css2?family=Arimo:wght@400;700&family=Noto+Serif&display=swap" rel="stylesheet">
<style>
:root{
  --teal:#2aafbf;
  --teal-dark:#1f97a6;
  --green:#b3d65a;
  --green-dark:#9cc23f;
  --text:#8a8a8a;
  --dark:#555;
  --light:#f2f2f2;
  --white:#fff;
}
*{box-sizing:border-box;margin:0;padding:0}
html,body{width:783px;height:1200px;overflow:hidden;background:var(--white);font-family:"Arimo",Arial,sans-serif;color:var(--text)}
.page{position:relative;width:783px;height:1200px}
.abs{position:absolute}

/* header */
.brand{left:99px;top:16px;display:flex;align-items:center;gap:8px}
.brand-mark{width:34px;height:34px;border-radius:50%;background:var(--green)}
.brand-name{color:var(--teal);font-size:18px;line-height:17px}
.brand-name small{display:block;font-size:11px;letter-spacing:1px}
.util-links{right:147px;top:8px;font-size:7.5px;color:#999;white-space:nowrap;text-align:right}
.util-links span{margin:0 3px}
.login{left:641px;top:4px;width:44px;height:15px;background:var(--green);color:var(--white);font-size:9px;text-align:center;line-height:15px}
.search-input{left:526px;top:38px;width:109px;height:15px;border:1px solid #ddd;background:#f7f7f7}
.search-btn{left:636px;top:38px;width:49px;height:15px;background:var(--teal);color:var(--white);font-size:9px;text-align:center;line-height:15px}

/* nav */
.nav{left:0;top:65px;width:783px;height:23px;background:var(--green)}
.nav ul{position:absolute;left:99px;top:0;display:flex;list-style:none;height:23px;border-left:1px solid rgba(255,255,255,.7)}
.nav li{color:var(--white);font-size:9px;line-height:23px;text-align:center;border-right:1px solid rgba(255,255,255,.7)}

/* hero */
.hero{left:0;top:88px;width:783px;height:266px;background:linear-gradient(100deg,#6a5a4c 0%,#b08a6a 25%,#8a6a5a 45%,#6a4a7a 70%,#4a8fa0 100%)}
.hero-caption{left:99px;top:305px;width:485px;height:49px;background:rgba(60,60,60,.75);color:var(--white);padding:6px 12px}
.hero-caption h2{font-size:11px;font-weight:400;margin-bottom:5px}
.hero-caption p{font-size:8px;line-height:10px}
.hero-dots{left:584px;top:305px;width:101px;height:49px;background:rgba(60,60,60,.6);display:flex;gap:5px;padding:23px 0 0 4px}
.hero-dots span{width:13px;height:13px;background:var(--green);color:var(--white);font-size:8px;text-align:center;line-height:13px}
.hero-dots span:nth-child(2){background:var(--teal)}

/* course cards */
.card{width:281px;height:123px;display:flex}
.card-photo{width:140px;height:123px}
.card-body{width:141px;background:var(--teal);color:var(--white);padding:10px 8px}
.card-body h3{font-size:11px;font-weight:400;line-height:13px;margin-bottom:2px}
.card-body p{font-size:8px;line-height:10px;text-align:justify}
.card-btn{display:inline-block;border:1px solid var(--white);font-size:8px;padding:2px 7px;margin-top:8px}

/* news */
.tab{left:98px;width:140px;height:25px;background:var(--green);color:var(--white);font-size:11px;line-height:25px;padding-left:9px}
.news-panel{left:238px;top:660px;width:448px;height:146px;background:var(--light);padding:6px}
.news-inner{background:var(--white);height:133px;display:grid;grid-template-columns:1fr 1fr;padding:8px 8px 0}
.news-item{display:flex;gap:6px;height:67px}
.news-icon{flex:none;width:20px;height:15px;margin-top:2px}
.news-item h4{color:var(--teal);font-size:7.5px;font-weight:400}
.news-item time{display:block;font-size:7px;font-style:italic;color:#999;margin:1px 0 3px}
.news-item p{font-size:7px;line-height:8.5px;text-align:justify;color:#777}

/* welcome */
.welcome{left:98px;top:826px;width:410px}
.welcome h1{font-family:"Noto Serif",Georgia,serif;font-weight:400;font-size:15px;color:var(--teal);margin-bottom:9px}
.welcome p{font-size:8.2px;line-height:10.2px;text-align:justify;color:#999;margin-bottom:10px}

/* calendar */
.calendar{left:544px;top:830px;width:141px}
.cal-head{height:19px;background:var(--teal);color:var(--white);font-size:9px;text-align:center;line-height:19px;position:relative}
.cal-head .prev{position:absolute;left:0;top:0;width:19px;height:19px;background:var(--teal-dark)}
.cal-head .next{position:absolute;right:0;top:0;width:19px;height:19px;background:var(--teal-dark)}
.cal-grid{display:grid;grid-template-columns:repeat(7,1fr)}
.cal-grid .dn{background:var(--teal);color:var(--white);font-size:6px;text-align:center;height:14px;line-height:14px;opacity:.9}
.cal-grid .d{height:20px;line-height:20px;text-align:center;font-size:7.5px;color:#444;background:#eee;border:1px solid var(--white)}
.cal-grid .muted{color:#bbb}
.cal-grid .today{background:#777;color:var(--white)}

/* subscribe */
.subscribe{left:0;top:1008px;width:783px;height:41px;background:var(--green)}
.subscribe p{position:absolute;left:98px;top:12px;color:var(--white);font-size:13px}
.sub-input{left:384px;top:1018px;width:164px;height:21px;background:var(--white);font-size:10px;color:#888;line-height:21px;padding-left:7px}
.sub-btn{left:552px;top:1018px;width:133px;height:21px;background:var(--green-dark);border:1px solid #8fb53a;color:var(--white);font-weight:700;font-size:10px;text-align:center;line-height:19px}

/* footer */
.footer{left:0;top:1049px;width:783px;height:130px;background:var(--light)}
.f-col{top:1069px}
.f-col h5{font-size:10px;font-weight:400;color:var(--teal);margin-bottom:10px}
.f-col p{font-size:7px;line-height:8.5px;color:#777;text-align:justify;margin-bottom:7px}
.f-col li{list-style:none;font-size:7px;color:#777;margin-bottom:6px;letter-spacing:.3px}
.f-contact li{display:flex;gap:6px;margin-bottom:8px;line-height:9px}
.socials{display:flex;gap:10px;margin-top:10px}
.socials span{width:20px;height:20px;border:2px solid #999;border-radius:50%}
.to-top{left:668px;top:1174px;width:17px;height:16px;background:#444;border-radius:2px}
.copyright{left:0;top:1179px;width:783px;height:21px;background:#e9e9e9;font-size:7px;color:#555;padding:7px 0 0 98px}
</style>
</head>
<body>
<div class="page">

  <header>
    <div class="abs brand"><span class="brand-mark"></span><span class="brand-name">Brisk Lyceum<small>for Gifted Youth</small></span></div>
    <div class="abs util-links">Blog<span>|</span>Jobs<span>|</span>Site Map<span>|</span>Accessibility</div>
    <div class="abs login">Login</div>
    <div class="abs search-input"></div>
    <div class="abs search-btn">Search</div>
  </header>

  <nav class="abs nav">
    <ul>
      <li style="width:53px">Home</li>
      <li style="width:61px">About Us</li>
      <li style="width:68px">Admission</li>
      <li style="width:69px">Academics</li>
      <li style="width:59px">Courses</li>
      <li style="width:84px">News / Events</li>
      <li style="width:53px">Results</li>
      <li style="width:65px">Fall 2013</li>
      <li style="width:74px">Contact Us</li>
    </ul>
  </nav>

  <section class="abs hero" role="img" aria-label="Photo of smiling students seated in a lecture hall"></section>
  <div class="abs hero-caption">
    <h2>Lorem ipsum dolor sit amet, consectetur adipiscing elit</h2>
    <p>Vestibulum faucibus augue at purus iaculis pulvinar. Phasellus at urna sagittis, facilisis quam et, pharetra augue. Vestibulum ante ipsum primis in faucibus orci</p>
  </div>
  <div class="abs hero-dots"><span>1</span><span>2</span><span>3</span><span>4</span><span>5</span></div>

  <article class="abs card" style="left:98px;top:375px">
    <div class="card-photo" role="img" aria-label="Photo of students doing a lab experiment" style="background:linear-gradient(135deg,#8a7a6a,#c9b89a 50%,#5a5048)"></div>
    <div class="card-body"><h3>SCIENCE COURSES</h3><p>Lorem ipsum dolor sit amet, consectetur adipiscing elit. Sed id tellus eget lorem mollis sdrge consequat vel vitae enim. Praesent aliquetnte.</p><span class="card-btn">Read More</span></div>
  </article>
  <article class="abs card" style="left:404px;top:375px">
    <div class="card-photo" role="img" aria-label="Photo of a hand holding a laptop with floating app tiles" style="background:linear-gradient(135deg,#1a2a3a,#4a7a9a 50%,#20303a)"></div>
    <div class="card-body"><h3>TECHNOLOGY<br>COURSES</h3><p>Lorem ipsum dolor sit amet, consectetur adipiscing elit. Sed id tellus eget lorem mollis sdrge consequat vel vitae enim. Praesent aliquetnte.</p><span class="card-btn">Read More</span></div>
  </article>
  <article class="abs card" style="left:98px;top:509px">
    <div class="card-body"><h3>ENGINEERING<br>COURSES</h3><p>Lorem ipsum dolor sit amet, consectetur adipiscing elit. Sed id tellus eget lorem mollis sdrge consequat vel vitae enim. Praesent aliquetnte.</p><span class="card-btn">Read More</span></div>
    <div class="card-photo" role="img" aria-label="Photo of hands drafting a technical drawing" style="background:linear-gradient(135deg,#e8e4de,#b8b0a8 50%,#d8d2ca)"></div>
  </article>
  <article class="abs card" style="left:404px;top:509px">
    <div class="card-body"><h3>MATH COURSES</h3><p>Lorem ipsum dolor sit amet, consectetur adipiscing elit. Sed id tellus eget lorem mollis sdrge consequat vel vitae enim. Praesent aliquetnte.</p><span class="card-btn">Read More</span></div>
    <div class="card-photo" role="img" aria-label="Photo of a green chalkboard covered in formulas" style="background:linear-gradient(135deg,#1d5a3e,#2a6e4c 50%,#184a34)"></div>
  </article>

  <div class="abs tab" style="top:661px">LATEST NEWS</div>
  <div class="abs tab" style="top:688px">UPCOMMING EVENTS</div>
  <section class="abs news-panel">
    <div class="news-inner">
      <div class="news-item"><svg class="news-icon" viewBox="0 0 20 15"><rect x="1" y="1" width="18" height="13" rx="2" fill="none" stroke="#2aafbf" stroke-width="1.5"/><rect x="4" y="4" width="5" height="4" fill="#2aafbf"/><path d="M11 5h5M11 8h5M4 11h12" stroke="#2aafbf"/></svg><div><h4>Lorem ipsum dolor sit amet, consectutur</h4><time>2013-06-02</time><p>Lorem ipsum dolor sit amet, consectetur adipiscing elit. Sed id tellus eget lorem mollis consequat vel vitae enim.</p></div></div>
      <div class="news-item"><svg class="news-icon" viewBox="0 0 20 15"><rect x="1" y="1" width="18" height="13" rx="2" fill="none" stroke="#2aafbf" stroke-width="1.5"/><rect x="4" y="4" width="5" height="4" fill="#2aafbf"/><path d="M11 5h5M11 8h5M4 11h12" stroke="#2aafbf"/></svg><div><h4>Lorem ipsum dolor sit amet, consectutur</h4><time>2013-06-02</time><p>Lorem ipsum dolor sit amet, consectetur adipiscing elit. Sed id tellus eget lorem mollis consequat vel vitae enim.</p></div></div>
      <div class="news-item"><svg class="news-icon" viewBox="0 0 20 15"><rect x="1" y="1" width="18" height="13" rx="2" fill="none" stroke="#2aafbf" stroke-width="1.5"/><rect x="4" y="4" width="5" height="4" fill="#2aafbf"/><path d="M11 5h5M11 8h5M4 11h12" stroke="#2aafbf"/></svg><div><h4>Lorem ipsum dolor sit amet, consectutur</h4><time>2013-06-02</time><p>Lorem ipsum dolor sit amet, consectetur adipiscing elit. Sed id tellus eget lorem mollis consequat vel vitae enim.</p></div></div>
      <div class="news-item"><svg class="news-icon" viewBox="0 0 20 15"><rect x="1" y="1" width="18" height="13" rx="2" fill="none" stroke="#2aafbf" stroke-width="1.5"/><rect x="4" y="4" width="5" height="4" fill="#2aafbf"/><path d="M11 5h5M11 8h5M4 11h12" stroke="#2aafbf"/></svg><div><h4>Lorem ipsum dolor sit amet, consectutur</h4><time>2013-06-02</time><p>Lorem ipsum dolor sit amet, consectetur adipiscing elit. Sed id tellus eget lorem mollis consequat vel vitae enim.</p></div></div>
    </div>
  </section>

  <section class="abs welcome">
    <h1>Welcome to Brisk Lyceum For Gifted Youth</h1>
    <p>Lorem ipsum dolor sit amet, consectetur adipiscing elit. Nulla eu porta lorem. Cras turpis ipsum, iaculis ut auctor eget, euismod eget enim. Curabitur a lorem porttitor lectus euismod semper vitae eu purus.</p>
    <p>Lorem ipsum dolor sit amet, consectetur adipiscing elit. Nulla eu porta lorem. Cras turpis ipsum, iaculis ut auctor eget, euismod eget enim. Curabitur a lorem porttitor lectus euismod semper vitae eu purus. Nulla at mi scelerisque urna dapibus ornare. Vestibulum ante ipsum primis in faucibus orci luctus et ultrices posuere cubilia Curae; Aliquam nec lectus elit, at aliquam est. Proin eget laoreet lectus.</p>
    <p>Nullam scelerisque cursus leo at volutpat. Etiam non faucibus ante. Ut eget leo placerat velit imperdiet suscipit. , at aliquam est. Proin eget laoreet lectus. Nullam scelerisque cursus leo at volutpat. Etiam non faucibus ante. Ut eget leo placerat velit imperdiet suscipit. at aliquam est.</p>
  </section>

  <aside class="abs calendar">
    <div class="cal-head">
      <span class="prev"><svg width="19" height="19" viewBox="0 0 19 19"><path d="M11 6l-4 3.5 4 3.5" fill="none" stroke="#fff" stroke-width="2"/></svg></span>
      JANUARY
      <span class="next"><svg width="19" height="19" viewBox="0 0 19 19"><path d="M8 6l4 3.5-4 3.5" fill="none" stroke="#fff" stroke-width="2"/></svg></span>
    </div>
    <div class="cal-grid">
      <span class="dn">SUN</span><span class="dn">MON</span><span class="dn">TUE</span><span class="dn">WED</span><span class="dn">THU</span><span class="dn">FRI</span><span class="dn">SAT</span>
      <span class="d">1</span><span class="d">2</span><span class="d">3</span><span class="d">4</span><span class="d">5</span><span class="d">6</span><span class="d">7</span>
      <span class="d">8</span><span class="d">9</span><span class="d">10</span><span class="d">11</span><span class="d">12</span><span class="d">13</span><span class="d">14</span>
      <span class="d">15</span><span class="d">16</span><span class="d">17</span><span class="d">18</span><span class="d">19</span><span class="d today">20</span><span class="d">21</span>
      <span class="d">22</span><span class="d">23</span><span class="d">24</span><span class="d">25</span><span class="d">26</span><span class="d">27</span><span class="d">28</span>
      <span class="d">29</span><span class="d">30</span><span class="d">31</span><span class="d muted">1</span><span class="d muted">2</span><span class="d muted">3</span><span class="d muted">4</span>
    </div>
  </aside>

  <section class="abs subscribe"><p>Stay in touch by email for updates and offers</p></section>
  <div class="abs sub-input">Your Email Here...</div>
  <div class="abs sub-btn">SUBSCRIBE NOW</div>

  <footer class="abs footer"></footer>
  <div class="abs f-col" style="left:98px;width:134px">
    <h5>About Us</h5>
    <p>Lorem ipsum dolor sit amet, consectetur adipiscing elit. Vivamus sit amet ligula vel diam congue semper.</p>
    <p>Ligula vel diam congue semper.Lorem ipsum dolor sit amet, consectetur adipiscing elit. Vivamus</p>
  </div>
  <div class="abs f-col" style="left:262px">
    <h5>Courses Offer</h5>
    <ul><li>&gt;&nbsp; Science Courses</li><li>&gt;&nbsp; Technolgy Courses</li><li>&gt;&nbsp; Engineering Courses</li><li>&gt;&nbsp; Math Courses</li></ul>
  </div>
  <div class="abs f-col f-contact" style="left:388px">
    <h5>Contact Us</h5>
    <ul>
      <li><svg width="10" height="9" viewBox="0 0 10 9"><path d="M5 0L0 4.5h1.5V9h2.5V6h2v3h2.5V4.5H10z" fill="#999"/></svg><span>820 Quarry Lane, Suite 14<br>Lakeford, CA 90000-1234</span></li>
      <li><svg width="10" height="9" viewBox="0 0 10 9"><path d="M2 0h2l1 2.5-1.5 1c.6 1.2 1.5 2.1 2.5 2.5l1-1.5L9.5 5.5v2L8 9C4 9 0 5 0 1.5z" fill="#999"/></svg><span>(555) 014-2287</span></li>
      <li><svg width="10" height="9" viewBox="0 0 10 9"><rect x="0" y="1" width="10" height="7" fill="#999"/><path d="M0 1l5 4 5-4" fill="none" stroke="#f2f2f2"/></svg><span>info@brisklyceum-example.com</span></li>
    </ul>
  </div>
  <div class="abs f-col" style="left:550px;width:136px">
    <h5>Stay In Touch</h5>
    <p>Follow US in our social networks! Lorem ipsum dolor sit amet, consectetur and go adipiscing elit.</p>
    <div class="socials"><span></span><span></span><span></span></div>
  </div>
  <div class="abs to-top"><svg width="17" height="16" viewBox="0 0 17 16"><path d="M4.5 10l4-4 4 4" fill="none" stroke="#fff" stroke-width="2"/></svg></div>
  <div class="abs copyright">Copyright © 2000-2013 , Brisk Lyceum for Gifted Youth.</div>

</div>
</body>
</html>
```